Business Card for Marriage Commissioner

I am a marriage commissioner in the province of Alberta, meaning that I perform civil unions here. I have been trying to think of a unique design for my business card, something a bit different. A lot of "unique" designs seem to incorporate unique cuts or "some assembly required" or printed on plastic or meat. I would like my design to be a full colour card that is a typical business card size.

The information on the card should have:
Lon Varbeck
my occupation: Marriage Commissioner
my website: www.lonvarbeck.ca
my e-mail: lon@lonvarbeck.ca
my phone: 780-914-2086

I originally submitted a design to the printer that had a screen capture of a finduro search window, with my name and occupation in the text box. And underneath that, my phone number. Nothing else. They indicated they could not print this because it was a copyright violation.

One option on the design is I am a retired chemist-so a chemistry themed card would also be of interest, as long as it isn't a "Quiet Reagent" theme, as I have that on my other business cards already...

I would prefer a single sided card, but I am open to a double sided card if it is clever!

I would also prefer not to have pictures of male and female couples as in my position I will also marry same sex couples. Same thing for male/female symbols. Someone has submitted two graduated cylinders in love, which is very clever, and gets around this male/female type.

Thanks for your help and interest.

Target Market(s)

Young couples.

Industry/Entity Type

Plastic

Requirements
Nice to have
• chemistry ideas!
Should not have
• Male/female pictures, male/female symbols.
No QR codes.
No transparent designs, will go on paper stock.

```html
<!DOCTYPE html>
<html lang="en">
<head>
<meta charset="utf-8">
<title>Lon Varbeck — Marriage Commissioner</title>
<link rel="stylesheet" href="https://fonts.googleapis.com/css2?family=Marcellus+SC&family=Arimo:wght@400&family=Pathway+Gothic+One&display=swap">
<style>
  :root {
    --page-bg: #e4e6e9;
    --card-black: #0b0b0c;
    --card-mid: #1c1c1e;
    --stripe: rgba(255,255,255,0.035);
    --panel: #050505;
    --text-white: #f4f4f4;
    --text-soft: #e2e2e2;
    --rule-dark: #000000;
    --rule-light: #2a2a2c;
  }
  * { margin: 0; padding: 0; box-sizing: border-box; }
  html, body {
    width: 1200px; height: 1199px; overflow: hidden;
    background: var(--page-bg);
  }
  .business-card {
    position: absolute;
    left: 75px; top: 300px;
    width: 1050px; height: 600px;
    overflow: hidden;
    background:
      repeating-linear-gradient(90deg, var(--stripe) 0 2px, transparent 2px 6px),
      radial-gradient(ellipse 70% 60% at 45% 20%, var(--card-mid), var(--card-black) 80%);
    box-shadow: 0 10px 30px rgba(0,0,0,0.25);
  }
  .accent-rules {
    position: absolute; top: 0; bottom: 0; left: 896px; width: 52px;
  }
  .accent-rules span { position: absolute; top: 0; bottom: 0; }
  .accent-rules .rule-a { left: 0; width: 10px; background: var(--rule-dark); }
  .accent-rules .rule-b { left: 10px; width: 4px; background: var(--rule-light); }
  .accent-rules .rule-c { left: 24px; width: 14px; background: var(--rule-dark); }
  .accent-rules .rule-d { left: 38px; width: 3px; background: var(--rule-light); }

  .name-plate {
    position: absolute; left: 0; top: 71px;
    width: 660px; height: 130px;
    background: var(--panel);
    border-radius: 0 18px 18px 0;
    text-align: center;
    padding-top: 14px;
    padding-left: 10px;
  }
  .holder-name {
    font-family: "Marcellus SC", serif;
    font-size: 58px; line-height: 1;
    letter-spacing: 4px;
    color: var(--text-white);
  }
  .holder-role {
    font-family: "Arimo", sans-serif;
    font-size: 36px; line-height: 1.2;
    color: var(--text-soft);
    margin-top: 4px;
  }

  .contact-rail {
    position: absolute; left: 60px; top: 323px;
    width: 107px; height: 300px;
    background: var(--panel);
    border-radius: 18px 18px 0 0;
  }
  .contact-list { list-style: none; position: absolute; left: 0; top: 0; }
  .contact-item {
    position: absolute; left: 0;
    display: flex; align-items: center;
    white-space: nowrap;
  }
  .contact-item .icon { position: absolute; left: 90px; width: 50px; display: flex; justify-content: center; }
  .contact-item .value {
    position: absolute; left: 194px;
    font-family: "Pathway Gothic One", sans-serif;
    font-size: 42px; color: var(--text-white);
    transform: translateY(-50%);
  }
  .contact-phone { top: 386px; }
  .contact-email { top: 459px; }
  .contact-web { top: 530px; }
  .contact-item svg { fill: var(--text-white); transform: translateY(-50%); }
</style>
</head>
<body>
  <div class="business-card">
    <div class="accent-rules">
      <span class="rule-a"></span><span class="rule-b"></span>
      <span class="rule-c"></span><span class="rule-d"></span>
    </div>

    <div class="name-plate">
      <h1 class="holder-name">Lon Varbeck</h1>
      <p class="holder-role">Marriage Commissioner</p>
    </div>

    <div class="contact-rail"></div>
    <ul class="contact-list">
      <li class="contact-item contact-phone">
        <span class="icon">
          <svg width="50" height="38" viewBox="0 0 50 38" aria-hidden="true">
            <path d="M4 12 C4 4 46 4 46 12 L46 16 L36 16 L36 11 L14 11 L14 16 L4 16 Z"/>
            <path d="M12 18 L38 18 L46 34 L4 34 Z"/>
            <circle cx="25" cy="26" r="5" fill="#050505"/>
          </svg>
        </span>
        <span class="value">780-914-2086</span>
      </li>
      <li class="contact-item contact-email">
        <span class="icon">
          <svg width="44" height="30" viewBox="0 0 44 30" aria-hidden="true">
            <rect x="1" y="1" width="42" height="28" fill="none" stroke="#f4f4f4" stroke-width="3"/>
            <path d="M2 2 L22 18 L42 2" fill="none" stroke="#f4f4f4" stroke-width="3"/>
          </svg>
        </span>
        <span class="value">lon@lonvarbeck.ca</span>
      </li>
      <li class="contact-item contact-web">
        <span class="icon">
          <svg width="38" height="38" viewBox="0 0 38 38" aria-hidden="true" fill="none" stroke="#f4f4f4" stroke-width="2.5">
            <circle cx="19" cy="19" r="16"/>
            <ellipse cx="19" cy="19" rx="7" ry="16"/>
            <line x1="3" y1="19" x2="35" y2="19"/>
            <line x1="19" y1="3" x2="19" y2="35"/>
            <path d="M6 10 H32 M6 28 H32"/>
          </svg>
        </span>
        <span class="value">www.lonvarbeck.ca</span>
      </li>
    </ul>
  </div>
</body>
</html>
```